New Business Card Design Project

I need a clean, professional business card. I'd like it to have some color, but not be wild. We do technology consulting and we have clients large and small who trust us with some of their most important data and projects. Simple but not boring should drive all design proposals. Multicolored and two sided, but with a matte finish, I think.
For more on tone, check out our website: http://quorvantis.example

Target Market(s)

Upper management of respected businesses. Tech savvy, but not "hipster".

Industry/Entity Type

Business

Requirements
Must have
• Files need to be provided in .eps and in .pdf in a manner that allows for easy updates.
Must have Name, Title, Phone, Email, Twitter, Website
Nice to have
• Logo/Name shouldn't be too big. One thing I've read several places is that the bigger the logo, the smaller the brand. A good article on dos and don'ts here: http://www.brindlepost.example/2011/02/business-card-experience.html

```html
<!DOCTYPE html>
<html lang="en">
<head>
<meta charset="utf-8">
<title>Quorvantis – Business Card</title>
<link rel="stylesheet" href="https://fonts.googleapis.com/css2?family=Fira+Sans:ital,wght@0,300;0,400;1,300;1,400&display=swap">
<style>
  :root {
    --teal: #3db3a7;
    --lime: #7dd300;
    --lime-soft: #b8e08c;
    --slate: #6c7a7a;
    --slate-light: #7d8888;
    --paper: #ffffff;
    --edge: #e2e4e4;
  }
  * { margin: 0; padding: 0; box-sizing: border-box; }
  html, body {
    width: 1200px; height: 900px; overflow: hidden;
    background: var(--paper);
    font-family: "Fira Sans", Arial, sans-serif;
  }
  .card {
    position: absolute; left: 74px; top: 138px;
    width: 1046px; height: 598px;
    background: var(--paper);
    border: 1px solid var(--edge);
  }
  .card > * { position: absolute; line-height: 1; white-space: nowrap; }
  .brand {
    right: 72px; top: 80px;
    display: flex; align-items: center; gap: 18px;
  }
  .brand-mark { width: 14px; height: 14px; background: var(--teal); }
  .brand-name {
    font-size: 56px; font-weight: 400; letter-spacing: 3px;
    color: var(--slate);
  }
  .accent-bar { left: 0; top: 168px; width: 974px; height: 18px; background: var(--lime); }
  .divider { left: 532px; top: 299px; width: 3px; height: 299px; background: var(--lime-soft); }
  .tagline {
    right: 546px; top: 296px; text-align: right;
    font-size: 45px; font-style: italic; font-weight: 300;
    color: var(--teal); line-height: 49px;
  }
  .tagline .highlight { color: var(--lime); }
  .contact { right: 72px; text-align: right; color: var(--slate); font-weight: 300; }
  .name { top: 229px; font-size: 36px; color: var(--teal); font-weight: 400; }
  .title { top: 273px; font-size: 28px; font-style: italic; color: var(--slate-light); }
  .phone { top: 364px; font-size: 30px; }
  .email { top: 413px; font-size: 30px; }
  .social { top: 463px; font-size: 30px; }
  .website { top: 513px; font-size: 30px; }
</style>
</head>
<body>
  <main class="card">
    <div class="brand">
      <span class="brand-mark"></span>
      <span class="brand-name">QUORVANTIS</span>
    </div>
    <div class="accent-bar"></div>
    <div class="divider"></div>
    <p class="tagline">unleashing the<br><span class="highlight">power</span> of information</p>
    <p class="contact name">Dana Morrell</p>
    <p class="contact title">Cheif Operating Officer</p>
    <p class="contact phone">(800) 555-0142</p>
    <p class="contact email">dana@quorvantis.example</p>
    <p class="contact social">Twitter: @quorvantist</p>
    <p class="contact website">www.quorvantis.example</p>
  </main>
</body>
</html>
```